Ridgeline Outfitters Business Cards

Recently had a logo done with Artflockr and now looking for a business card to go along with it.

Target Market(s)

Ridgeline Outfitters is a weapons dealer. My market will be primarily men, hunting, shooting type.

Industry/Entity Type

Business

Contact Information for Business Card

I selected double sided, but this is not required, single or double is going to be fine. I picture the logo on one side, or perhaps just the circle which contains "RO" with the remaining info on the other side.

Font styles to use
Sans Serif

Requirements
Must have
• My name: Wesley Holm
• Title: Owner
• tel: 612-555-0378
• web: www.ridgelineoutfittersmn.example
Nice to have
• I like the concept of a black business card. I would like to keep the colors monotone, black, grey, white or red. Red is acceptable because it is in the logo. I have also seen cards that are matte black with shiny black as well, perhaps for the logo (or circle RO) part of the logo.
• I will upload a couple of the logos for use, and also an example I just found of the black on black. and some others that have a nice contrast.
Should not have
• lots of colors are not wanted.

```html
<!DOCTYPE html>
<html lang="en">
<head>
<meta charset="utf-8">
<title>Ridgeline Outfitters Business Cards</title>
<link rel="stylesheet" href="https://fonts.googleapis.com/css2?family=Montserrat:wght@500;700&display=swap">
<style>
  :root {
    --bg: #8a7563;
    --card-black: #050505;
    --brand-red: #ee1c25;
    --steel-grey: #5f5f5f;
    --ring-grey: #6b6b6b;
    --name-grey: #7a7a7a;
    --white: #ffffff;
  }
  * { margin: 0; padding: 0; box-sizing: border-box; }
  html, body { width: 1200px; height: 866px; overflow: hidden; }
  body {
    background: var(--bg);
    font-family: "Montserrat", sans-serif;
    position: relative;
  }
  .card {
    position: absolute;
    width: 580px;
    height: 331px;
    background: var(--card-black);
    overflow: hidden;
    box-shadow: 0 10px 24px rgba(0,0,0,0.35);
  }
  .card-front { left: 130px; top: 80px; }
  .card-back { left: 500px; top: 450px; }
  .card-shapes { position: absolute; inset: 0; width: 100%; height: 100%; }

  .brand-lockup {
    position: absolute;
    left: 150px;
    top: 132px;
    display: flex;
    align-items: center;
    gap: 16px;
  }
  .brand-ring {
    width: 64px; height: 64px;
    border-radius: 50%;
    border: 4px solid var(--ring-grey);
  }
  .brand-name {
    color: var(--brand-red);
    font-weight: 700;
    font-size: 22px;
    letter-spacing: 1px;
    text-transform: uppercase;
  }

  .back-mark {
    position: absolute;
    left: 472px; top: 18px;
    width: 56px; height: 56px;
    border-radius: 50%;
    border: 4px solid var(--ring-grey);
    display: flex; align-items: center; justify-content: center;
    color: var(--brand-red);
    font-weight: 700;
    font-size: 18px;
  }
  .person { position: absolute; left: 36px; top: 86px; }
  .person-name { font-size: 22px; font-weight: 700; color: var(--white); line-height: 1; }
  .person-name .surname { color: var(--name-grey); }
  .person-title { font-size: 15px; font-weight: 500; color: var(--brand-red); margin-top: 3px; letter-spacing: 0.5px; }

  .contact-bar {
    position: absolute;
    display: flex;
    align-items: center;
    height: 28px;
    background: var(--steel-grey);
    color: var(--white);
    font-weight: 700;
    letter-spacing: 2px;
  }
  .contact-phone { left: 46px; top: 150px; font-size: 16px; letter-spacing: 3px; padding-right: 12px; }
  .contact-web { left: 60px; top: 206px; font-size: 13px; padding-right: 12px; }
  .contact-icon {
    width: 30px; height: 28px;
    display: flex; align-items: center; justify-content: center;
    margin-right: 12px;
  }
  .contact-phone .contact-icon { background: var(--white); }
</style>
</head>
<body>

<section class="card card-front" aria-label="Business card front">
  <svg class="card-shapes" viewBox="0 0 580 331" aria-hidden="true">
    <polygon points="0,0 130,0 0,290" fill="var(--brand-red)"/>
    <polygon points="410,0 580,0 580,250" fill="var(--steel-grey)"/>
  </svg>
  <div class="brand-lockup">
    <span class="brand-ring"></span>
    <span class="brand-name">Ridgeline Outfitters</span>
  </div>
</section>

<section class="card card-back" aria-label="Business card back">
  <svg class="card-shapes" viewBox="0 0 580 331" aria-hidden="true">
    <polygon points="0,0 68,0 0,62" fill="var(--brand-red)"/>
    <rect x="462" y="0" width="80" height="14" fill="var(--steel-grey)"/>
    <polygon points="450,96 520,86 566,331 478,331" fill="var(--steel-grey)"/>
    <polygon points="552,170 580,152 580,331 572,331" fill="var(--brand-red)"/>
    <polygon points="440,331 474,268 486,331" fill="var(--brand-red)"/>
  </svg>
  <div class="back-mark">RO</div>

  <div class="person">
    <p class="person-name">Wesley <span class="surname">Holm</span></p>
    <p class="person-title">Owner</p>
  </div>

  <div class="contact-bar contact-phone">
    <span class="contact-icon">
      <svg width="18" height="18" viewBox="0 0 24 24" aria-hidden="true">
        <path fill="#5f5f5f" d="M6.6 10.8c1.4 2.8 3.8 5.1 6.6 6.6l2.2-2.2c.3-.3.7-.4 1-.2 1.1.4 2.3.6 3.6.6.6 0 1 .4 1 1V20c0 .6-.4 1-1 1C10.6 21 3 13.4 3 4c0-.6.4-1 1-1h3.5c.6 0 1 .4 1 1 0 1.3.2 2.5.6 3.6.1.3 0 .7-.2 1z"/>
      </svg>
    </span>
    612-555-0378
  </div>

  <div class="contact-bar contact-web">
    <span class="contact-icon">
      <svg width="20" height="20" viewBox="0 0 24 24" aria-hidden="true">
        <circle cx="12" cy="12" r="10" fill="var(--white)"/>
        <path d="M12 2a10 10 0 0 1 0 20M12 2a10 10 0 0 0 0 20M2 12h20M12 2c3 3 3 17 0 20M12 2c-3 3-3 17 0 20" fill="none" stroke="#5f5f5f" stroke-width="1.4"/>
      </svg>
    </span>
    www.ridgelineoutfittersmn.example
  </div>
</section>

</body>
</html>
```